Wedding Dried Apple Label / Name Place Card

We are looking for a simple but stylish label to be attached via string to a bag of dried apples from my family's fruit farm. The size of the label we think should be similar to the size of a business card. The packaging will be a plastic bag: 4" x 2" x 6".
We would like it to say something like:
Corin & Tessa
Est. Sept 10, 2017
Dried Apple Slices
Product of Marrow Orchard Farm
________________
(We need a spot to write in the name of the person and a table number)
Our colors are also grey and navy, and would like these colors to be used.
We have uploaded a photo of the plastic bag.

```html
<!DOCTYPE html>
<html lang="en">
<head>
<meta charset="utf-8">
<title>Corin &amp; Tessa – Dried Apple Slices Label</title>
<link rel="stylesheet" href="https://fonts.googleapis.com/css2?family=Great+Vibes&family=Zilla+Slab:wght@300;600&family=Montserrat:wght@600&display=swap">
<style>
  :root {
    --navy: #22508a;
    --white: #ffffff;
    --grey: #b5b5b5;
    --grey-text: #a9a9a9;
    --wreath-dark: #5e3f38;
    --wreath-mid: #8a6155;
    --wreath-light: #a88272;
  }
  html, body {
    margin: 0;
    padding: 0;
    overflow: hidden;
    background: var(--navy);
  }
  .label {
    display: block;
    width: 686px;
    height: 1200px;
    background: var(--navy);
  }
  .names {
    font-family: "Great Vibes", cursive;
    fill: var(--navy);
  }
  .arc-text {
    font-family: "Zilla Slab", serif;
    font-weight: 300;
    fill: var(--grey-text);
    letter-spacing: 3px;
  }
  .product-of, .table-label {
    font-family: "Zilla Slab", serif;
    font-weight: 600;
    fill: var(--grey-text);
    letter-spacing: 2px;
  }
  .farm-name {
    font-family: "Montserrat", sans-serif;
    font-weight: 600;
    fill: var(--white);
    letter-spacing: 2.5px;
  }
</style>
</head>
<body>
<svg class="label" width="686" height="1200" viewBox="0 0 686 1200" xmlns="http://www.w3.org/2000/svg">
  <defs>
    <radialGradient id="wreath-tone" cx="50%" cy="50%" r="50%">
      <stop offset="78%" stop-color="var(--wreath-light)"/>
      <stop offset="88%" stop-color="var(--wreath-mid)"/>
      <stop offset="100%" stop-color="var(--wreath-dark)"/>
    </radialGradient>
    <path id="arc-top" d="M 176 380 A 166 166 0 0 1 508 380"/>
    <path id="arc-bottom" d="M 170 376 A 174 174 0 0 0 518 376"/>
    <path id="arc-ribbon" d="M 150 906 Q 346 850 542 906"/>
  </defs>

  <!-- Round tag -->
  <g class="round-tag">
    <circle cx="344" cy="372" r="332" fill="var(--white)"/>
    <circle cx="344" cy="372" r="314" fill="none" stroke="var(--grey)" stroke-width="9"/>
    <circle class="wreath" role="img" aria-label="Watercolour twig wreath with red and green apples"
            cx="342" cy="372" r="262" fill="none" stroke="url(#wreath-tone)" stroke-width="52" stroke-opacity="0.85"/>

    <text class="arc-text" font-size="24">
      <textPath href="#arc-top" startOffset="50%" text-anchor="middle">EST. OCTOBER•21•2019</textPath>
    </text>
    <text class="arc-text" font-size="25">
      <textPath href="#arc-bottom" startOffset="50%" text-anchor="middle">DRIED APPLE SLICES</textPath>
    </text>

    <text class="names" x="166" y="362" font-size="124">corin</text>
    <text class="names" x="228" y="472" font-size="120">&amp; tessa</text>
  </g>

  <!-- Place card -->
  <g class="place-card">
    <rect x="26" y="760" width="640" height="410" rx="48" fill="var(--white)"/>
    <rect x="45" y="777" width="602" height="376" rx="40" fill="none" stroke="var(--grey)" stroke-width="10"/>

    <text class="product-of" x="346" y="820" font-size="29" text-anchor="middle">PRODUCT OF:</text>

    <g class="ribbon" fill="var(--navy)">
      <path d="M 140 900 L 94 946 L 132 950 L 118 998 L 178 962 Z"/>
      <path d="M 552 900 L 598 946 L 560 950 L 574 998 L 514 962 Z"/>
      <path d="M 136 868 Q 346 800 556 868 L 556 944 Q 346 876 136 944 Z"/>
    </g>
    <text class="farm-name" font-size="19">
      <textPath href="#arc-ribbon" startOffset="50%" text-anchor="middle">• MARROW ORCHARD FARM •</textPath>
    </text>

    <line class="name-line" x1="96" y1="1057" x2="596" y2="1057" stroke="var(--grey)" stroke-width="2"/>
    <text class="table-label" x="168" y="1118" font-size="29">TABLE Nº:</text>
    <line class="table-line" x1="320" y1="1124" x2="560" y2="1124" stroke="var(--grey)" stroke-width="2"/>
  </g>
</svg>
</body>
</html>
```